Corvin Staffing Partners Business Cards

Business cards with logo design for a new recruiting company called "Corvin Staffing Partners"

incorporate RED & BLUE colors

Final design should reflect strength - clean, elegant design

Company name superimposed upon graphic (Greek Columns)

Please see attached Photos!!!

Industry/Entity Type

Business

Font styles to use
Decorative

Colors
ec2027
0555a3
85cae6

Requirements
Must have
• Must look very similar to attached design!!!

Want Company name superimposed upon graphic (Greek Columns)

Tag line at bottom must be included:
"Strengthening Remarkable Employers with Remarkable Talent"

```html
<!DOCTYPE html>
<html lang="en">
<head>
<meta charset="utf-8">
<title>Corvin Staffing Partners – Business Card</title>
<link rel="stylesheet" href="https://fonts.googleapis.com/css2?family=Caladea:wght@400;700&display=swap">
<style>
  :root {
    --brand-red: #ec2027;
    --brand-blue: #0555a3;
    --brand-sky: #85cae6;
    --ink: #222222;
    --divider: #f4c9c9;
    --card: #ffffff;
    --backdrop: #e9e7e3;
  }
  * { box-sizing: border-box; margin: 0; padding: 0; }
  html, body {
    width: 1200px;
    height: 845px;
    overflow: hidden;
    background: var(--backdrop);
    font-family: "Caladea", Georgia, serif;
  }
  .business-card {
    position: absolute;
    left: 75px;
    top: 122px;
    width: 1050px;
    height: 600px;
    background: var(--card);
    box-shadow: 0 10px 30px rgba(0, 0, 0, 0.18);
  }
  .brand {
    position: absolute;
    left: 62px;
    top: 52px;
    display: flex;
    align-items: flex-start;
    gap: 22px;
  }
  .brand-dot {
    width: 58px;
    height: 58px;
    margin-top: 8px;
    border-radius: 50%;
    background: var(--brand-sky);
  }
  .brand-name {
    color: var(--brand-blue);
    font-size: 46px;
    line-height: 1.12;
    font-weight: 400;
  }
  .tagline {
    position: absolute;
    left: 62px;
    bottom: 48px;
    color: var(--brand-red);
    font-size: 29px;
    line-height: 1.22;
  }
  .tagline span { display: block; }
  .tagline span:nth-child(2) { padding-left: 8px; }
  .tagline span:nth-child(3) { padding-left: 16px; }
  .contact-divider {
    position: absolute;
    left: 612px;
    top: 272px;
    width: 2px;
    height: 290px;
    background: var(--divider);
  }
  .contact {
    position: absolute;
    left: 640px;
    top: 290px;
  }
  .contact-name {
    color: var(--brand-blue);
    font-size: 42px;
    font-weight: 400;
    margin-bottom: 42px;
  }
  .contact-list { list-style: none; }
  .contact-list li {
    display: flex;
    align-items: center;
    gap: 14px;
    color: var(--ink);
    font-size: 25px;
    margin-bottom: 14px;
  }
  .contact-icon { width: 26px; height: 26px; flex: none; }
</style>
</head>
<body>
  <main class="business-card">
    <div class="brand">
      <div class="brand-dot"></div>
      <div class="brand-name">Corvin<br>Staffing<br>Partners</div>
    </div>

    <p class="tagline">
      <span>Strengthening</span>
      <span>Remarkable Employers</span>
      <span>with Remarkable Talent</span>
    </p>

    <div class="contact-divider"></div>

    <section class="contact">
      <h1 class="contact-name">Daniel R. Whitmore</h1>
      <ul class="contact-list">
        <li>
          <svg class="contact-icon" viewBox="0 0 26 26" aria-hidden="true">
            <circle cx="13" cy="13" r="12" fill="none" stroke="#222" stroke-width="2"/>
            <path d="M9 7 l3 0 l1 3 l-2 1.5 a8 8 0 0 0 3.5 3.5 l1.5 -2 l3 1 l0 3 a2 2 0 0 1 -2 1.5 a11 11 0 0 1 -9.5 -9.5 a2 2 0 0 1 1.5 -2 z" fill="#222"/>
          </svg>
          512-555-0148
        </li>
        <li>
          <svg class="contact-icon" viewBox="0 0 26 26" aria-hidden="true">
            <rect x="2" y="7" width="22" height="14" rx="2" fill="#222"/>
            <path d="M3 8 l10 8 l10 -8" fill="none" stroke="#fff" stroke-width="1.8"/>
          </svg>
          DWhitmore@CorvinSP.com
        </li>
        <li>
          <svg class="contact-icon" viewBox="0 0 26 26" aria-hidden="true">
            <circle cx="13" cy="13" r="11" fill="#222"/>
            <g fill="none" stroke="#fff" stroke-width="1.4">
              <ellipse cx="13" cy="13" rx="5" ry="11"/>
              <line x1="2" y1="13" x2="24" y2="13"/>
              <path d="M4 8 h18 M4 18 h18"/>
            </g>
          </svg>
          www.CorvinSP.com
        </li>
      </ul>
    </section>
  </main>
</body>
</html>
```